Label or packaging Design for Hair Care Line

Dear Designer,
We are Corvella, a brand known for our premium hairstyling tools, and we are excited to expand into hair care. We are currently looking for a talented designer to create the label designs for our entire luxury hair care line.
This project is crucial in establishing our visual identity in the hair care market, and we aim to position ourselves alongside premium brands such as LTP, Dorvane Hair Atelier, and Pelmi.
Project Scope
We need a cohesive label design for our hair care line, which includes:
5 products (e.g., shampoo, conditioner, hair oil, styling cream, and a hair mask).
The designs should include:
Front label: Highlighting the product name, key features, and branding.
Our goal is to achieve a design that communicates premium luxury with a touch of professionalism. Below are the specific guidelines to help you align with our vision:
Style and Inspiration
Think of brands like LTP, Dorvane Hair Atelier, and Pelmi.
Luxury and Minimalism: Clean lines, sophisticated typography, and an elegant color palette.
Subtle femininity: premium finishes like metallic accents (gold, silver, or rose gold).
Brand Personality
Premium: Reflecting high quality and exclusivity.
Modern & Professional: Appealing to a refined, professional audience but also suitable for lifestyle-oriented customers.
Warm & Empowering: A brand that celebrates confidence and individuality.
Color Palette
Neutral tones like black, white, accented with metallics (gold or silver) for a luxurious feel.
Colors that feel timeless and elegant rather than trendy or overly bright.
Typography
Use clean, modern fonts (preferably sans-serif or serif for a refined look).
Clear and legible for all product details while maintaining a high-end aesthetic.
Materials and Finishes
Packaging Shape
The label designs should suit a variety of bottle and jar shapes (e.g., cylindrical, flat, or rounded).
Keep scalability in mind so the identity remains consistent across different products.
Deliverables
To understand the aesthetic we are aiming for, here are some brands to use as inspiration:
LTP: For its minimalistic and modern approach.
Dorvane Hair Atelier: For its combination of luxury and professional appeal.
Pelmi: For its soft femininity and lifestyle branding.
we would like to see your designs applied to a variety of packaging types to get an overall impression of how the brand identity works across different product formats. This includes:
A squeeze bottle (e.g., for styling creams or conditioners).
A glass bottle with a dropper (e.g., for a luxurious hair oil).
A shampoo/conditioner bottle (standard pump or flip-top cap).
A spray bottle (e.g., for leave-in treatments or heat protectors).
By creating designs for these different packaging types, we can better evaluate how cohesive and versatile the brand identity will be across the entire product line.

Updates
As you may have noticed from the designs, they don’t quite align with our briefing. The look needs to be clean and professional, similar to Dorvane, LTP, and the other examples we provided. Please address this, and we’ll check it!

Target Market(s)
europe and us
Font styles to use
Other font styles liked:
- century gothic

Look and feel
Each slider illustrates characteristics of the customer's brand and the style your logo design should communicate.

```html
<!DOCTYPE html>
<html lang="en">
<head>
<meta charset="utf-8">
<title>Corvella Radiance – Front Label</title>
<link rel="stylesheet" href="https://fonts.googleapis.com/css2?family=Barlow:wght@400;500;700&display=swap">
<style>
  :root {
    --page: #ffffff;
    --label-bg: #ffffff;
    --ink: #111111;
    --label-edge: #2a2a2a;
    --marble-light: #f1f1f1;
    --marble-mid: #c9c9c9;
    --marble-dark: #8f8f8f;
  }
  * { margin: 0; padding: 0; box-sizing: border-box; }
  html, body {
    width: 924px;
    height: 1200px;
    overflow: hidden;
    background: var(--page);
  }
  .canvas {
    position: relative;
    width: 924px;
    height: 1200px;
    font-family: "Barlow", sans-serif;
    color: var(--ink);
  }
  .label {
    position: absolute;
    left: 32px;
    top: 110px;
    width: 860px;
    height: 979px;
    background: var(--label-bg);
    border: 1.5px solid var(--label-edge);
    overflow: hidden;
  }
  .label__marble {
    position: absolute;
    left: 0;
    top: 0;
    width: 100%;
    height: 521px;
    background:
      radial-gradient(ellipse 40% 30% at 25% 30%, var(--marble-dark) 0%, transparent 70%),
      radial-gradient(ellipse 35% 40% at 75% 45%, var(--marble-mid) 0%, transparent 75%),
      linear-gradient(135deg, var(--marble-light) 0%, var(--marble-mid) 45%, var(--marble-light) 100%);
  }
  .brand-box {
    position: absolute;
    left: 263px;
    top: 282px;
    width: 333px;
    height: 322px;
    border: 11px solid var(--ink);
    background: var(--label-bg);
    display: flex;
    flex-direction: column;
    align-items: center;
    text-align: center;
    padding-top: 44px;
  }
  .brand-box__name {
    font-size: 62px;
    font-weight: 400;
    line-height: 1;
    letter-spacing: 1px;
  }
  .brand-box__line {
    margin-top: 18px;
    font-size: 27px;
    font-weight: 400;
    letter-spacing: 3px;
  }
  .brand-box__claims {
    margin-top: 20px;
    font-size: 16px;
    font-weight: 500;
    letter-spacing: 9px;
    line-height: 1.55;
    padding-left: 9px;
  }
  .label__product {
    position: absolute;
    left: 0;
    width: 100%;
    top: 836px;
    text-align: center;
  }
  .label__product-type {
    font-size: 14px;
    font-weight: 700;
    letter-spacing: 0.5px;
  }
  .label__volume {
    margin-top: 4px;
    font-size: 19px;
    font-weight: 400;
    letter-spacing: 2px;
  }
</style>
</head>
<body>
  <main class="canvas">
    <section class="label">
      <div class="label__marble" role="img" aria-label="Grey and white swirling liquid marble pattern"></div>

      <div class="brand-box">
        <p class="brand-box__name">Corvella</p>
        <p class="brand-box__line">RADIANCE</p>
        <p class="brand-box__claims">REFINE<br>RESTORE<br>REVEAL</p>
      </div>

      <div class="label__product">
        <p class="label__product-type">SHAMPOO AND CONDITIONER</p>
        <p class="label__volume">60 ML / 2.05 OZ</p>
      </div>
    </section>
  </main>
</body>
</html>
```